Magazine Design 6 page front and back

Would like the frame work of a design template for a 12page magazine. Looking to be able to change out the images and edit myself down the road as I complete new projects.

I would like a re-design of the attached magazine to get an entire different feel. I would like more elegant. I have attached a KVR flyer just for the colors not for the layout, I attached my business card design. I attached the flyer magazine that I made just for the informational content.

This magazine is to display my experience and expertise in the business along with customer testimonials.

Will this design be a design template that I can change out the images or wording on? As I do more and more design I would like to keep updating it with new content.

I have quite a few images that I can upload but I'm not sure of the process do you create the template and them start putting in the photos?

Target Market(s)

High end Spas, Country Club, Private facilities

Industry/Entity Type

Fitness Equipment sales and Design

Colors
0054AA
0677BA
7BADD7
CADEEF
E8F1F8

Requirements
Must have
• Elegant high end feel. I would like the small logo implemented somewhere like how it is on the back of my business card.

```html
<!DOCTYPE html>
<html lang="en">
<head>
<meta charset="utf-8">
<title>Summit Form Studio – Statement of Qualification</title>
<link href="https://fonts.googleapis.com/css2?family=Signika:wght@400;600;700&family=Open+Sans:wght@400;600;700&display=swap" rel="stylesheet">
<style>
:root{
  --blue-deep:#0054AA;
  --blue:#0677BA;
  --blue-mid:#7BADD7;
  --blue-pale:#CADEEF;
  --blue-mist:#E8F1F8;
  --title-blue:#2f6fb5;
  --ink:#0b0b0c;
  --charcoal:#2a2a2b;
  --slate:#3a3a3c;
  --stage:#c4c6c5;
  --body-text:#3b3b3b;
  --placeholder-dark:#3d4249;
}
*{box-sizing:border-box;margin:0;padding:0}
html,body{width:1200px;height:2806px;overflow:hidden}
body{background:var(--stage);font-family:"Open Sans",Arial,sans-serif;position:relative}
.spread{position:absolute;left:110px;width:980px;height:634px;display:flex;box-shadow:0 6px 14px rgba(0,0,0,.25)}
.page{position:relative;width:490px;height:100%;overflow:hidden}
.divider{position:absolute;left:490px;top:0;width:1px;height:100%;background:#888;z-index:5}

/* ---------- cover ---------- */
.cover{background:linear-gradient(90deg,#4a4848 0%,#1a1a1b 30%,#000 60%,#0b0b0c 100%);overflow:hidden}
.cover-band{position:absolute;inset:0}
.cover-photo{position:absolute;left:455px;top:245px;width:445px;height:330px;background:linear-gradient(180deg,#5f97d6 0%,#a9c6e6 35%,#8f8a85 65%,#a06b45 100%)}
.brand-top{position:absolute;left:610px;top:58px;display:flex;align-items:center;gap:10px;font-family:"Signika",sans-serif;font-weight:600;font-size:22px;letter-spacing:1px;color:var(--title-blue)}
.brand-mark{width:14px;height:14px;background:var(--title-blue)}
.cover-id{position:absolute;left:128px;top:330px;color:#fff}
.cover-id .brand-name{font-family:"Signika",sans-serif;font-weight:600;font-size:19px;letter-spacing:1px;display:flex;align-items:center;gap:8px}
.cover-id .brand-name span.mark{width:12px;height:12px;background:#fff}
.contact{list-style:none;margin:22px 0 0 52px;font-family:"Signika",sans-serif;font-weight:600;font-size:8px;line-height:12px}
.contact li{display:flex;align-items:center;gap:6px}
.contact li::before{content:"";width:7px;height:7px;border-radius:50%;background:var(--blue)}
.cover-title{position:absolute;left:588px;top:580px;font-family:"Signika",sans-serif;font-weight:700;font-size:18px;letter-spacing:1px;color:#fff}

/* ---------- page head / foot ---------- */
.page-head{position:absolute;left:0;top:0;width:490px;height:40px}
.head-brand{position:absolute;left:16px;top:17px;font-family:"Signika",sans-serif;font-weight:600;font-size:6.5px;letter-spacing:.3px;display:flex;align-items:center;gap:4px;color:var(--title-blue)}
.head-brand i{display:block;width:7px;height:7px;background:var(--title-blue)}
.head-band{position:absolute;left:0;top:0}
.head-title{position:absolute;right:12px;top:20px;font-family:"Signika",sans-serif;font-weight:700;font-size:12.5px;letter-spacing:.6px;color:var(--title-blue)}
.url{font-family:"Signika",sans-serif;font-size:7px;font-weight:600;color:var(--blue-deep)}

/* ---------- profile page ---------- */
.page--light{background:#fff}
.profile{position:absolute;left:47px;top:65px;width:285px;color:var(--body-text);font-size:6.1px;line-height:8.4px}
.profile h2{font-family:"Signika",sans-serif;font-weight:700;font-size:13px;color:var(--title-blue);letter-spacing:.5px;margin:0 0 6px}
.profile h3{font-family:"Signika",sans-serif;font-weight:700;font-size:12.5px;color:var(--title-blue);margin:12px 0 6px}
.profile p{margin-bottom:6px}
.services{list-style:none;margin-top:6px}
.services li{display:flex;align-items:center;gap:12px;font-family:"Signika",sans-serif;font-weight:600;font-size:7px;color:#222;height:22px}
.services li::before{content:"";width:7px;height:5px;border:1.5px solid var(--blue);border-radius:1px}
.plan{position:absolute;left:190px;top:440px;width:220px;height:150px;background:linear-gradient(160deg,#e9edf0,#b9c2c8 60%,#dfe4e7)}
.sidebar{position:absolute;left:338px;top:78px;width:122px;height:325px;background:var(--blue-pale);text-align:center;padding:6px 8px;font-size:5.3px;line-height:7.5px;color:#333}
.sidebar h4{font-family:"Signika",sans-serif;font-weight:700;font-size:5.6px;color:#1b2a3a;border-bottom:1px solid var(--blue);padding-bottom:2px;margin:0 0 3px}
.sidebar p{margin-bottom:10px}
.portrait{position:absolute;left:14px;top:240px;width:94px;height:72px;background:linear-gradient(180deg,#f2f2f2,#c9ccd0)}
.sidebar .caption{position:absolute;left:0;bottom:5px;width:100%;font-size:5.3px;line-height:7px}
.sidebar .caption b{font-family:"Signika",sans-serif;color:#1b2a3a}
.light-foot{position:absolute;left:0;top:605px;width:490px;height:30px}
.light-foot .url{position:absolute;left:0;right:0;top:612px}

/* ---------- project page ---------- */
.page--dark{background:#fff}
.dark-top{position:absolute;left:0;top:0;width:490px;height:252px;background:var(--ink)}
.project-band{position:absolute;left:0;top:64px}
.project-title{position:absolute;left:40px;top:70px;font-family:"Signika",sans-serif;font-weight:700;font-size:27px;letter-spacing:1.5px;color:#fff;white-space:nowrap}
.project-place{position:absolute;left:40px;top:106px;font-family:"Signika",sans-serif;font-weight:700;font-size:11px;letter-spacing:.8px;color:#fff}
.project-copy{position:absolute;left:40px;top:147px;width:410px;font-size:6.6px;line-height:9px;color:#d8d8d8}
.photo{position:absolute;background:linear-gradient(135deg,#4a4f57,#2e3137 50%,#8b8e92)}
.photo--hero{left:40px;top:262px;width:368px;height:144px}
.photo--a{left:40px;top:412px;width:119px;height:125px}
.photo--b{left:165px;top:412px;width:119px;height:125px}
.photo--c{left:290px;top:412px;width:119px;height:125px}
.dark-foot{position:absolute;left:0;top:572px;width:490px;height:63px;background:var(--ink)}
.page-num{position:absolute;left:238px;top:14px;width:13px;height:13px;border:1px solid var(--blue);border-radius:50%;font-size:5px;color:var(--blue-mid);display:flex;align-items:center;justify-content:center}
.foot-rule{position:absolute;left:0;top:34px}
.dark-foot .url{position:absolute;left:0;right:0;top:38px;text-align:center}
</style>
</head>
<body>

<!-- cover spread (shown twice, as in the presentation) -->
<section class="spread cover" style="top:70px">
  <svg class="cover-band" width="980" height="634" viewBox="0 0 980 634">
    <defs><linearGradient id="bandA" x1="0" x2="1"><stop offset="0" stop-color="#0a4f86"/><stop offset=".55" stop-color="#1d8fd6"/><stop offset="1" stop-color="#0a5d93"/></linearGradient></defs>
    <polygon points="210,150 980,150 980,634 190,634 250,520 210,420" fill="url(#bandA)"/>
  </svg>
  <div class="cover-photo" role="img" aria-label="Photo of a modern multi-storey residential building with stone and wood facade under a blue sky"></div>
  <div class="brand-top"><span class="brand-mark"></span>SUMMIT FORM STUDIO</div>
  <div class="cover-id">
    <div class="brand-name"><span class="mark"></span>SUMMIT FORM STUDIO</div>
    <ul class="contact"><li>ND. SD. MN. NE. IA. KS</li><li>555 014 2870</li><li>/dalemarrow</li><li>dale@summitform.example</li><li>www.summitform.example</li></ul>
  </div>
  <div class="cover-title">STATEMENT OF QUALIFICATION</div>
</section>

<section class="spread cover" style="top:754px">
  <svg class="cover-band" width="980" height="634" viewBox="0 0 980 634">
    <defs><linearGradient id="bandB" x1="0" x2="1"><stop offset="0" stop-color="#0a4f86"/><stop offset=".55" stop-color="#1d8fd6"/><stop offset="1" stop-color="#0a5d93"/></linearGradient></defs>
    <polygon points="210,150 980,150 980,634 190,634 250,520 210,420" fill="url(#bandB)"/>
  </svg>
  <div class="cover-photo" role="img" aria-label="Photo of a modern multi-storey residential building with stone and wood facade under a blue sky"></div>
  <div class="brand-top"><span class="brand-mark"></span>SUMMIT FORM STUDIO</div>
  <div class="cover-id">
    <div class="brand-name"><span class="mark"></span>SUMMIT FORM STUDIO</div>
    <ul class="contact"><li>ND. SD. MN. NE. IA. KS</li><li>555 014 2870</li><li>/dalemarrow</li><li>dale@summitform.example</li><li>www.summitform.example</li></ul>
  </div>
  <div class="cover-title">STATEMENT OF QUALIFICATION</div>
</section>

<!-- spread: company profile + project -->
<section class="spread" style="top:1417px">
  <article class="page page--light">
    <header class="page-head">
      <svg class="head-band" width="490" height="40"><polygon points="92,34 108,20 490,20 490,34" fill="#333"/></svg>
      <div class="head-brand"><i></i>SUMMIT FORM</div>
      <div class="head-title">COMPANY PROFILE</div>
    </header>
    <div class="profile">
      <h2>PROFILE</h2>
      <p>Summit Form Studio specializes in fitness, sports performance, park and rec, government, multi-housing, and private clubs and has been servicing Nebraska, Iowa, South Dakota, North Dakota and the surrounding area for over 22 years.</p>
      <p>Our long-standing and proven track record with our customers and extraordinary product knowledge has helped us become the leading service provider in our area for brands such as Stepcraft, Norvane, FlexMotion, ReStride, Cyclon, Astra Trac, SciMove, Vireo and many more.</p>
      <p>Our consistency, professionalism and dedication to our customers sets us apart from our competitors. We provide timely, efficient, thorough and unparalleled service to our customers and we would like the opportunity to provide our industry leading service and manufacturers to you.</p>
      <p>We will provide you with industry leading equipment and an outstanding customer experience, as well as the ability to respond your needs in a timely manner. We have the resources to meet the demands of your fitness, rehabilitation and athletic needs.</p>
      <h3>Dale Marrow Consultant</h3>
      <p>My portfolio contains a broad range of projects, including municipal, education, recreation and wellness, health care, private clubs, government and military, mixed-used, multi-family residential, sports performance, corporate, hotels and renovation projects.</p>
      <p>My goal is to layout for you a facility that is functional and cost effective – I believe that the success of my past projects has resulted from effective collaboration my clients Engineers, Architects and clients and user groups. I am passionate about creative, collaborative and problem-solving design. More importantly, we are committed to client satisfaction. I ask a lot of questions, and I do more listening than talking so that I can understand what is important to you and what you need.</p>
      <h3>SERVICES PROVIDED</h3>
      <ul class="services"><li>3-D Design Concepts</li><li>Equipment Procurement</li><li>Equipment Service</li><li>Complementary Consults</li><li>Technology Design</li><li>Industry Concepts</li></ul>
    </div>
    <div class="plan" role="img" aria-label="3-D rendered floor plan of a fitness facility with labelled equipment zones"></div>
    <aside class="sidebar">
      <h4>WHAT GYM CLIENTS NEED</h4>
      <p>One-of-a-kind fitness facility to make their property stand out. Someone who manages the process of creating, visualizing, selecting, and bringing all necessary aspects of the project to completion.</p>
      <h4>THE DESIGN PROCESS</h4>
      <p>Getting to know the space, surrounding area, and purpose of the facility before beginning the in-depth process of equipment selection and visualization.</p>
      <h4>WHY IT MATTERS</h4>
      <p>Gym design consulting services will help you discover what competitors are doing, understand current market trends, and how to best utilize the current space so you can be the leader in luxury fitness facilities.</p>
      <div class="portrait" role="img" aria-label="Portrait photo of the consultant"></div>
      <div class="caption"><b>CONSULTANT</b><br>(C) 555-014-2870<br>support@summitform.example</div>
    </aside>
    <svg class="light-foot" width="490" height="30" viewBox="0 0 490 30"><polygon points="0,0 200,0 210,10 0,10" fill="#333"/><polygon points="285,10 295,0 490,0 490,10" fill="#333"/></svg>
    <div class="url" style="position:absolute;left:190px;top:613px">www.summitform.example</div>
  </article>

  <article class="page page--dark">
    <div class="dark-top"></div>
    <header class="page-head">
      <svg class="head-band" width="490" height="40"><polygon points="92,34 108,20 490,20 490,34" fill="#3a3a3c"/></svg>
      <div class="head-brand"><i></i>SUMMIT FORM</div>
      <div class="head-title">RIDGELINE ATHLETIC</div>
    </header>
    <svg class="project-band" width="490" height="190" viewBox="0 0 490 190">
      <defs><linearGradient id="pbA" x1="0" x2="1"><stop offset="0" stop-color="#0a5d93"/><stop offset=".6" stop-color="#1f8fd3"/><stop offset="1" stop-color="#0b5f99"/></linearGradient></defs>
      <polygon points="0,0 490,0 475,70 0,70" fill="url(#pbA)"/>
      <polygon points="0,70 475,70 490,66 470,188 0,188" fill="#2a2a2b"/>
    </svg>
    <div class="project-title">RIDGELINE ATHLETIC</div>
    <div class="project-place">OMAHA / NEBRASKA</div>
    <p class="project-copy">Ridgeline Athletic is a private health space in Omaha, NE that provides specifically curated, customized small group and functional fitness based programs for its members. Owner Lena Hart had a clear vision to develop the space and sought me to fulfill it. The facility features a thoughtfully planned functional training ecosystem including Korvex Fitness wall configurations for dynamic training. The heart of the space is optimize for personal and small group training, customized rubber floor covering, cardio and strength training zones, and plentiful accessories round out the training floor offering.</p>
    <div class="photo photo--hero" role="img" aria-label="Gym floor with strength racks and cardio machines in front of a red feature wall"></div>
    <div class="photo photo--a" role="img" aria-label="Cable strength machine in the gym"></div>
    <div class="photo photo--b" role="img" aria-label="Row of treadmills facing a dark wall"></div>
    <div class="photo photo--c" role="img" aria-label="Strength stations on rubber flooring"></div>
    <footer class="dark-foot">
      <div class="page-num">01</div>
      <svg class="foot-rule" width="490" height="6"><rect width="490" height="6" fill="#3a3a3c"/></svg>
      <div class="url">www.summitform.example</div>
    </footer>
  </article>
  <div class="divider"></div>
</section>

<!-- spread: two projects -->
<section class="spread" style="top:2084px">
  <article class="page page--dark">
    <div class="dark-top"></div>
    <header class="page-head">
      <svg class="head-band" width="490" height="40"><polygon points="92,34 108,20 490,20 490,34" fill="#3a3a3c"/></svg>
      <div class="head-brand"><i></i>SUMMIT FORM</div>
      <div class="head-title">RIVERBEND ACTIVITY CENTER</div>
    </header>
    <svg class="project-band" width="490" height="190" viewBox="0 0 490 190">
      <defs><linearGradient id="pbB" x1="0" x2="1"><stop offset="0" stop-color="#0a5d93"/><stop offset=".6" stop-color="#1f8fd3"/><stop offset="1" stop-color="#0b5f99"/></linearGradient></defs>
      <polygon points="0,0 490,0 475,70 0,70" fill="url(#pbB)"/>
      <polygon points="0,70 475,70 490,66 470,188 0,188" fill="#2a2a2b"/>
    </svg>
    <div class="project-title" style="font-size:24px">RIVERBEND ACTIVITY CENTER</div>
    <div class="project-place">JAMESTOWN / NORTH DAKOTA</div>
    <p class="project-copy">The facility, includes an outdoor swimming pools, a gymnasium, an indoor jogging track, dance and aerobics rooms, multipurpose rooms. The center offers a dynamic environment for popular fitness, recreational, enrichment and social activities for all ages whether it be for children, young adults, adults, and senior citizens. The design of the center provides for the integration and interaction of people from all age groups so that everyone may share in the fun, socialization and learning that intergenerational experiences bring.</p>
    <div class="photo photo--hero" style="background:linear-gradient(135deg,#d9d6d0,#8a8784 50%,#c9c5be)" role="img" aria-label="Bright cardio room with rows of ellipticals and bikes"></div>
    <div class="photo photo--a" style="background:linear-gradient(135deg,#e3e1dc,#a9a6a1)" role="img" aria-label="Recumbent bikes in a fitness room"></div>
    <div class="photo photo--b" style="background:linear-gradient(135deg,#d8d4cc,#9c978f)" role="img" aria-label="Strength machines on a tiled floor"></div>
    <div class="photo photo--c" style="background:linear-gradient(135deg,#cfcbc4,#7e7a74)" role="img" aria-label="Cardio machines by a window"></div>
    <footer class="dark-foot">
      <div class="page-num">02</div>
      <svg class="foot-rule" width="490" height="6"><rect width="490" height="6" fill="#3a3a3c"/></svg>
      <div class="url">www.summitform.example</div>
    </footer>
  </article>

  <article class="page page--dark">
    <div class="dark-top"></div>
    <header class="page-head">
      <svg class="head-band" width="490" height="40"><polygon points="92,34 108,20 490,20 490,34" fill="#3a3a3c"/></svg>
      <div class="head-brand"><i></i>SUMMIT FORM</div>
      <div class="head-title">PRAIRIE TECHNICAL COLLEGE</div>
    </header>
    <svg class="project-band" width="490" height="190" viewBox="0 0 490 190">
      <defs><linearGradient id="pbC" x1="0" x2="1"><stop offset="0" stop-color="#0a5d93"/><stop offset=".6" stop-color="#1f8fd3"/><stop offset="1" stop-color="#0b5f99"/></linearGradient></defs>
      <polygon points="0,0 490,0 475,70 0,70" fill="url(#pbC)"/>
      <polygon points="0,70 475,70 490,66 470,188 0,188" fill="#2a2a2b"/>
    </svg>
    <div class="project-title" style="font-size:24px">PRAIRIE TECHNICAL COLLEGE</div>
    <div class="project-place">MITCHELL / SOUTH DAKOTA</div>
    <p class="project-copy">Prairie Technical College wanted to keep their students safe and on campus and be able to live a healthy lifestyle. Cultivating a healthy relationship with fitness for personal well being is vital for every individual and more so with college students due to the increased high rates of stress. Prairie Technical Colleges new wellness center features high quality cardio equipment, strength equipment as well as a movement space. The outcome is a design-driven approach built around the growing demand for many different cardio and strength modalities to keep students engaged.</p>
    <div class="photo photo--hero" style="background:linear-gradient(135deg,#6d9a3a,#3b4a35 45%,#9b9994)" role="img" aria-label="Stair climbers in front of a green graphic wall"></div>
    <div class="photo photo--a" style="background:linear-gradient(135deg,#8fb05a,#4b5447)" role="img" aria-label="Strength racks beside a green wall graphic"></div>
    <div class="photo photo--b" style="background:linear-gradient(135deg,#7ea34b,#505a52)" role="img" aria-label="Cardio machines in the wellness center"></div>
    <div class="photo photo--c" style="background:linear-gradient(135deg,#b8b6b0,#6a6c6e)" role="img" aria-label="Strength equipment near large windows"></div>
    <footer class="dark-foot">
      <div class="page-num">03</div>
      <svg class="foot-rule" width="490" height="6"><rect width="490" height="6" fill="#3a3a3c"/></svg>
      <div class="url">www.summitform.example</div>
    </footer>
  </article>
  <div class="divider"></div>
</section>

</body>
</html>
```